Marketing company needs business card design

Our company (Ventures Beyond Harbor) need a business card design for a marketing company. The design should of course include the logo and business colors (orange and blue). I would like the design to be clean and professional. The business card is going to be a die cut card that is leaf shaped (I have uploaded the template for it). I would love to see a design that is professional but nothing too "corporate."
Updates

Hello everyone,

Just wanted to let you know that I have uploaded an AI and EPS version of the logo for your convenience.

Thank you!

~Marlene

Industry/Entity Type

Marketing

Requirements
Must have
• Must have the following contact info:

Ventures Beyond Harbor
2817 Hollow Brook Ln B204
Millbrook, CO 86517

555.471.6083

info@venturesbeyondharbor-example.com

```html
<!DOCTYPE html>
<html lang="en">
<head>
<meta charset="utf-8">
<title>Ventures Beyond Harbor – Business Card</title>
<link rel="stylesheet" href="https://fonts.googleapis.com/css2?family=Open+Sans:wght@400;600;700&display=swap">
<style>
  :root {
    --bg: #ece8e3;
    --orange: #f2a65c;
    --blue: #1d8fd5;
    --sky-top: #2c5f9e;
    --sky-mid: #8fb6df;
    --sky-light: #e6f0fa;
    --ink: #1f1f1f;
    --white: #ffffff;
  }
  * { box-sizing: border-box; margin: 0; padding: 0; }
  html, body {
    width: 1200px; height: 960px; overflow: hidden;
    background: var(--bg);
    font-family: "Open Sans", Arial, sans-serif;
  }
  .canvas {
    position: relative; width: 1200px; height: 960px;
    display: flex; flex-direction: column; align-items: center; justify-content: center; gap: 60px;
  }
  .card {
    position: relative; width: 700px; height: 400px;
    background: var(--orange);
    border-radius: 0 170px 0 170px;
    overflow: hidden;
    box-shadow: 0 8px 24px rgba(0,0,0,0.15);
  }
  .card-art { position: absolute; inset: 0; width: 100%; height: 100%; }
  .logo-box {
    position: absolute;
    background: rgba(255,255,255,0.94);
    display: flex; align-items: center; justify-content: center; gap: 10px;
  }
  .logo-mark {
    width: 16px; height: 16px; border-radius: 50%;
    background: var(--orange); flex: none;
  }
  .logo-name {
    color: var(--blue); font-weight: 600; font-size: 19px; line-height: 1.15;
  }
  .front .logo-box { left: 55px; top: 235px; width: 215px; height: 95px; }
  .contact { position: absolute; left: 375px; top: 138px; color: var(--ink); }
  .contact-company { font-size: 21px; font-weight: 700; }
  .contact-address { font-size: 13.5px; font-weight: 600; line-height: 1.4; margin-top: 4px; }
  .contact-phone { font-size: 22px; font-weight: 700; margin-top: 28px; letter-spacing: 0.5px; }
  .contact-email { font-size: 12.5px; font-weight: 700; margin-top: 30px; }
  .back .logo-box { left: 225px; top: 135px; width: 250px; height: 120px; }
  .back .logo-name { font-size: 22px; }
</style>
</head>
<body>
<main class="canvas">
  <section class="card front" aria-label="Business card front">
    <svg class="card-art" viewBox="0 0 700 400" preserveAspectRatio="none">
      <defs>
        <linearGradient id="skyline" x1="0" y1="0" x2="0" y2="1">
          <stop offset="0" stop-color="var(--sky-top)"/>
          <stop offset="0.35" stop-color="var(--sky-mid)"/>
          <stop offset="0.55" stop-color="var(--sky-light)"/>
          <stop offset="1" stop-color="var(--sky-mid)"/>
        </linearGradient>
      </defs>
      <path class="accent-band" d="M0,0 H268 Q338,200 268,400 H0 Z" fill="var(--blue)"/>
      <path class="photo-area" role="img" aria-label="Photo of a bright city skyline under a cloudy blue sky"
            d="M0,0 H255 Q325,200 255,400 H0 Z" fill="url(#skyline)"/>
    </svg>
    <div class="logo-box">
      <span class="logo-mark"></span>
      <span class="logo-name">Ventures Beyond<br>Harbor</span>
    </div>
    <div class="contact">
      <p class="contact-company">Ventures Beyond Harbor</p>
      <p class="contact-address">2817 Hollow Brook Ln B204<br>Millbrook, CO 86517</p>
      <p class="contact-phone">555.471.6083</p>
      <p class="contact-email">info@venturesbeyondharbor-example.com</p>
    </div>
  </section>

  <section class="card back" aria-label="Business card back">
    <div class="logo-box">
      <span class="logo-mark"></span>
      <span class="logo-name">Ventures Beyond<br>Harbor</span>
    </div>
  </section>
</main>
</body>
</html>
```